I need a logo design for a new company based in Tucson called "Mindpilot Reg Holloway". I am a psychotherapist that specializes in clinical psychology with athletes and performers. The final design should incorporate the psychology symbol as a watermark. The logo should convey movement and fluidity. "Mindpilot" is a bit of a play on words combining psychology (head) with sports (coach). Other design interests include mid-century, Ansel Brigham Kotter. I will want to use the logo for business cards, letterhead and marketing brochures. I will put together a website at a later date. I am attaching a file with some pertinent information for the business card. Thank you.
Reg Holloway
mindpilotregholloway@quillmarsh.net
Updates

Thank you all for the submissions so far.  I have submitted an additional file with a draft of a new design idea.  Since "mindpilot" is a bit of a play on words, I would like to see something with the two "H's" look something like quotation marks.  If the psychology logo is to be included at all, it needs to be less prominent.     Thank you all.  Reg                               

Target Market(s)

1) Adolescent and adult athletes and performers who are looking to increase their level of performance (Sport and Performance Psychology)
2) Adult psychotherapy patients (Clinical psychology)

Industry/Entity Type

Marketing

Colors

Designer to choose colors to be used in the design.

Requirements
Must have
• 1) Since "mindpilot" is a bit of a play on words, The "H's" need to be in a font that looks somewhat like quotation marks.

Nice to have
• Logo on one side. All other info on the backside?

```html
<!DOCTYPE html>
<html lang="en">
<head>
<meta charset="utf-8">
<title>Mindpilot business cards</title>
<link href="https://fonts.googleapis.com/css2?family=Cinzel:wght@400&family=Marcellus&family=Open+Sans:wght@400;700&display=swap" rel="stylesheet">
<style>
  :root {
    --page: #e9e6e1;
    --card-white: #fbfbfb;
    --blue-deep: #124a6a;
    --blue-mid: #1d6a90;
    --blue-light: #2f85ad;
    --green: #a3c64a;
    --grey-text: #5a5a5a;
    --white: #ffffff;
  }
  * { box-sizing: border-box; margin: 0; padding: 0; }
  html, body { width: 1200px; height: 1023px; overflow: hidden; }
  body { background: var(--page); position: relative; font-family: "Open Sans", sans-serif; }

  .card {
    position: absolute;
    width: 520px;
    height: 298px;
    border-radius: 3px;
    overflow: hidden;
    box-shadow: 0 6px 18px rgba(0,0,0,0.18);
  }
  .card--front { left: 50px; top: 362px; background: var(--card-white); }
  .card--back {
    left: 630px; top: 362px;
    background: linear-gradient(135deg, var(--blue-light) 0%, var(--blue-mid) 45%, var(--blue-deep) 100%);
    display: flex; align-items: center; justify-content: center;
  }

  .brand-name {
    font-family: "Marcellus", serif;
    font-size: 58px;
    letter-spacing: 1px;
    line-height: 1;
  }
  .card--front .brand-name { color: var(--green); }
  .card--back .brand-name { color: var(--white); }

  .identity {
    position: absolute; left: 0; top: 0; width: 100%; height: 172px;
    display: flex; flex-direction: column; align-items: center; justify-content: center;
  }
  .identity .brand-name { font-size: 50px; margin-bottom: 20px; }
  .rule { width: 220px; height: 1px; background: var(--green); margin-bottom: 18px; }
  .person-name {
    font-family: "Cinzel", serif; color: var(--green);
    font-size: 20px; letter-spacing: 1px;
  }
  .person-title { font-size: 12px; color: var(--grey-text); margin-top: 2px; }

  .contact-band {
    position: absolute; left: 0; bottom: 0; width: 100%; height: 126px;
    background: linear-gradient(180deg, var(--blue-light) 0%, var(--blue-mid) 50%, var(--blue-deep) 100%);
    border-top: 3px solid var(--blue-deep);
    display: flex; justify-content: space-between; align-items: center;
    padding: 0 26px;
  }
  .contact-list { list-style: none; color: var(--white); font-size: 13px; }
  .contact-list li { display: flex; align-items: center; gap: 8px; margin: 5px 0; }
  .contact-icon { width: 14px; height: 14px; flex: none; }

  .practice { text-align: left; }
  .practice-focus { color: var(--green); font-weight: 700; font-size: 13px; line-height: 1.35; }
  .practice-address { color: var(--white); font-size: 12px; margin-top: 6px; }

  .back-logo { display: flex; flex-direction: column; align-items: center; }
  .back-logo .rule { background: var(--white); width: 230px; margin: 18px 0 0; }
</style>
</head>
<body>
  <section class="card card--front">
    <div class="identity">
      <div class="brand-name">mindpilot</div>
      <div class="rule"></div>
      <div class="person-name">Reginald H. Holloway MA</div>
      <div class="person-title">Licensed Professional Counselor</div>
    </div>
    <div class="contact-band">
      <ul class="contact-list">
        <li>
          <svg class="contact-icon" viewBox="0 0 14 14"><rect width="14" height="14" rx="1" fill="var(--green)"/><path d="M4 3.5h2l.6 2-1.1.8a5 5 0 0 0 2.2 2.2l.8-1.1 2 .6v2a1 1 0 0 1-1 1A7 7 0 0 1 3 4.5a1 1 0 0 1 1-1z" fill="var(--blue-deep)"/></svg>
          520.555.0148
        </li>
        <li>
          <svg class="contact-icon" viewBox="0 0 14 14"><rect width="14" height="14" rx="1" fill="var(--green)"/><rect x="3.5" y="5" width="7" height="5" fill="var(--blue-deep)"/><rect x="5" y="3" width="4" height="2.5" fill="var(--blue-deep)"/></svg>
          520.555.0172
        </li>
        <li>
          <svg class="contact-icon" viewBox="0 0 14 14"><rect width="14" height="14" rx="1" fill="var(--green)"/><rect x="3" y="4.5" width="8" height="5.5" fill="var(--blue-deep)"/><path d="M3 4.5l4 3 4-3" stroke="var(--green)" stroke-width="0.9" fill="none"/></svg>
          mindpilotregholloway@quillmarsh.net
        </li>
      </ul>
      <div class="practice">
        <div class="practice-focus">Clinical &amp; Athletic<br>Performance Psychology</div>
        <div class="practice-address">1450 West Quail Run #210<br>Tucson, AZ 85704</div>
      </div>
    </div>
  </section>

  <section class="card card--back">
    <div class="back-logo">
      <div class="brand-name">mindpilot</div>
      <div class="rule"></div>
    </div>
  </section>
</body>
</html>
```